Business Card Design Project

Colette Marvaux logo on front of card with 'of Sydney' added in small font.
Back of card needs to include the following information :

"Pure pleasure for the discerning gentleman" (I may omit once I've seen the design)

colettemarvaux.com.au

Contact by SMS or email only :

colette@colettemarvaux.com.au
Mobile : 0483 615 204 or + 61 483 615 204

Target Market(s)

Male professionals aged 20-60.

Industry/Entity Type

Business

Requirements
Must have
• Simple, bold, stylish and elegant.

```html
<!DOCTYPE html>
<html lang="en">
<head>
<meta charset="utf-8">
<title>Colette Marvaux – Business Card Options</title>
<link href="https://fonts.googleapis.com/css2?family=Didact+Gothic&family=Pinyon+Script&display=swap" rel="stylesheet">
<style>
  :root {
    --canvas: #ffffff;
    --card-front: #000000;
    --ink-dark: #111111;
    --ink-light: #ffffff;
    --ink-muted: #bdbdbd;
    --border-light: #9a9a9a;
    --sage: #6e7f78;
    --charcoal: #58585a;
    --card-w: 367px;
    --card-h: 243px;
  }
  * { margin: 0; padding: 0; box-sizing: border-box; }
  html, body {
    width: 1200px;
    height: 848px;
    overflow: hidden;
    background: var(--canvas);
  }
  .sheet {
    position: relative;
    width: 1200px;
    height: 848px;
  }
  .card {
    position: absolute;
    width: var(--card-w);
    height: var(--card-h);
  }
  .card--front {
    left: 224px;
    background: var(--card-front);
    display: flex;
    flex-direction: column;
    align-items: center;
    justify-content: center;
  }
  .card--back { left: 604px; }
  .row-1 { top: 51px; }
  .row-2 { top: 309px; }
  .row-3 { top: 565px; }

  .wordmark {
    font-family: "Didact Gothic", sans-serif;
    color: var(--ink-light);
    font-size: 21px;
    line-height: 26px;
    letter-spacing: 3px;
    text-transform: uppercase;
    margin-top: 10px;
  }
  .locale {
    font-family: "Didact Gothic", sans-serif;
    color: var(--ink-light);
    font-size: 11px;
    line-height: 14px;
    letter-spacing: 3px;
    text-transform: uppercase;
    margin-top: 6px;
  }

  .back--white { background: #fff; border: 1px solid var(--border-light); color: var(--ink-dark); }
  .back--sage { background: var(--sage); color: var(--ink-light); }
  .back--charcoal { background: var(--charcoal); color: var(--ink-light); }

  .tagline {
    position: absolute;
    left: 36px;
    top: 32px;
    font-family: "Pinyon Script", cursive;
    font-size: 29px;
    line-height: 27px;
  }
  .contact {
    position: absolute;
    top: 145px;
    font-family: "Didact Gothic", sans-serif;
    font-size: 12.6px;
    line-height: 14.4px;
  }
  .contact--web { left: 32px; }
  .contact--details { left: 174px; }
</style>
</head>
<body>
<main class="sheet">
  <section class="card card--front row-1">
    <span class="wordmark">Colette Marvaux</span>
    <span class="locale">of Sydney</span>
  </section>
  <section class="card card--back back--white row-1">
    <p class="tagline">Pure pleasure for the<br>discerning gentleman.</p>
    <p class="contact contact--web">colettemarvaux.com.au</p>
    <p class="contact contact--details">Contact by SMS or email<br>only please:<br>colette@colettemarvaux.com.au<br>0483 615 204 /<br>+ 61 483 615 204</p>
  </section>

  <section class="card card--front row-2">
    <span class="wordmark">Colette Marvaux</span>
    <span class="locale">of Sydney</span>
  </section>
  <section class="card card--back back--sage row-2">
    <p class="tagline">Pure pleasure for the<br>discerning gentleman.</p>
    <p class="contact contact--web">colettemarvaux.com.au</p>
    <p class="contact contact--details">Contact by SMS or email<br>only please:<br>colette@colettemarvaux.com.au<br>0483 615 204 /<br>+ 61 483 615 204</p>
  </section>

  <section class="card card--front row-3">
    <span class="wordmark">Colette Marvaux</span>
    <span class="locale">of Sydney</span>
  </section>
  <section class="card card--back back--charcoal row-3">
    <p class="tagline">Pure pleasure for the<br>discerning gentleman.</p>
    <p class="contact contact--web">colettemarvaux.com.au</p>
    <p class="contact contact--details">Contact by SMS or email<br>only please:<br>colette@colettemarvaux.com.au<br>0483 615 204 /<br>+ 61 483 615 204</p>
  </section>
</main>
</body>
</html>
```